Vesit cards for web development company

We need a business card design for our company. The company develops online platforms and conducts marketing consulting. Company logo. The cards must fit in with us (a junior start UP), but they must also be professional enough to impress with investors like banks. We wish you a combination of classic and modern design

Target Market(s)

Business partners and IT and marketing customers

Industry/Entity Type

It Company

Contact Information for Business Card

Folgende Information müssen Drauf.
Name, Position, Telefon Nr., Mobile Nr., E-Mail adresse, Optional sind noch Webadresse und HRB Nummer

Colors

Designer to choose colors to be used in the design.

Requirements
Must have
• The cards have to fit into the logo later and have to be dynamic and serious at the same time

```html
<!DOCTYPE html>
<html lang="en">
<head>
<meta charset="utf-8">
<title>Norvale Development – Business Card</title>
<link rel="stylesheet" href="https://fonts.googleapis.com/css2?family=Open+Sans:wght@400;600;700&display=swap">
<style>
  :root {
    --page-bg: #e9ebee;
    --card-white: #f7f7f6;
    --brand-blue: #1273bd;
    --divider-grey: #9c9fa3;
    --text-white: #ffffff;
    --rule-light: rgba(255,255,255,0.6);
  }
  * { box-sizing: border-box; margin: 0; padding: 0; }
  html, body {
    width: 1200px; height: 900px; overflow: hidden;
    background: var(--page-bg);
    font-family: "Open Sans", Arial, sans-serif;
  }
  .business-card {
    position: absolute; left: 160px; top: 178px;
    width: 880px; height: 544px;
    background: var(--card-white);
    box-shadow: 0 10px 30px rgba(0,0,0,0.15);
    overflow: hidden;
  }
  .brand-area {
    height: 310px;
    display: flex; align-items: center; justify-content: center; gap: 16px;
    padding-top: 20px;
  }
  .brand-dot {
    width: 30px; height: 30px; border-radius: 50%;
    background: var(--brand-blue);
  }
  .brand-name {
    color: var(--brand-blue);
    font-weight: 700; font-size: 46px; letter-spacing: 1px;
    text-transform: uppercase;
  }
  .grey-band { height: 7px; background: var(--divider-grey); }
  .contact-band {
    position: relative; height: 227px;
    background: var(--brand-blue); color: var(--text-white);
  }
  .contact-list {
    position: absolute; right: 459px; top: 50px;
    list-style: none; text-align: right;
  }
  .contact-list li {
    display: flex; align-items: center; justify-content: flex-end; gap: 12px;
    font-size: 22px; line-height: 32px;
  }
  .contact-list svg { width: 18px; height: 18px; flex: none; }
  .band-divider {
    position: absolute; left: 470px; top: 56px;
    width: 1px; height: 114px; background: var(--rule-light);
  }
  .person {
    position: absolute; left: 503px; top: 42px;
  }
  .person-name { font-size: 37px; font-weight: 400; line-height: 1.2; }
  .person-role { font-size: 21px; line-height: 1.3; }
  .register-number { margin-top: 26px; font-size: 22px; }
</style>
</head>
<body>
  <div class="business-card">
    <div class="brand-area">
      <span class="brand-dot"></span>
      <span class="brand-name">Norvale Development</span>
    </div>
    <div class="grey-band"></div>
    <div class="contact-band">
      <ul class="contact-list">
        <li>044-987 654 321
          <svg viewBox="0 0 18 18" aria-hidden="true"><rect x="5" y="1" width="8" height="16" rx="1.5" fill="none" stroke="#fff" stroke-width="1.6"/><rect x="7.5" y="13.5" width="3" height="1.5" fill="#fff"/></svg>
        </li>
        <li>044-987 654 322
          <svg viewBox="0 0 18 18" aria-hidden="true"><path d="M2 8c0-3 3-5 7-5s7 2 7 5l-3 1-1-2H6L5 9z" fill="#fff"/><rect x="4" y="10" width="10" height="6" rx="1" fill="#fff"/></svg>
        </li>
        <li>hello@norvale.dev
          <svg viewBox="0 0 18 18" aria-hidden="true"><rect x="1" y="4" width="16" height="11" fill="#fff"/><path d="M1 4l8 6 8-6" fill="none" stroke="#1273bd" stroke-width="1.4"/></svg>
        </li>
        <li>www.norvale.dev
          <svg viewBox="0 0 18 18" aria-hidden="true"><circle cx="9" cy="9" r="8" fill="#fff"/><path d="M5 6c2 0 3 1 2 3s1 3 0 5M12 4c-1 2 1 3 2 4" fill="none" stroke="#1273bd" stroke-width="1.4"/></svg>
        </li>
      </ul>
      <div class="band-divider"></div>
      <div class="person">
        <p class="person-name">Daniel Kerr</p>
        <p class="person-role">Managing Director</p>
        <p class="register-number">HRB NUMBER: 731206</p>
      </div>
    </div>
  </div>
</body>
</html>
```